Tutorial design for a website

Design the tutorial as a PDF following the design of brindlequay.io
The website is already designed we need the tutorial to follow the llok and feel.

```html
<!DOCTYPE html>
<html lang="en">
<head>
<meta charset="utf-8">
<title>Step 3 – Open Futures Account</title>
<link rel="stylesheet" href="https://fonts.googleapis.com/css2?family=Montserrat:wght@500;600;700;800&family=Playfair+Display:wght@700&family=Inter:wght@500;600;700&display=swap">
<style>
:root{
  --bg:#22252a;
  --lime:#d4f55e;
  --ink:#1b1d21;
  --white:#ffffff;
  --ui-bg:#171a1f;
  --ui-panel:#1f2329;
  --ui-text:#eaecef;
  --ui-muted:#848e9c;
  --ui-yellow:#f0b90b;
  --ui-red:#f6465d;
  --marker:#ff2a1a;
}
*{margin:0;padding:0;box-sizing:border-box}
html,body{width:1200px;height:800px;overflow:hidden;background:var(--bg)}
.page{position:relative;width:1200px;height:800px;background:var(--bg);font-family:"Montserrat",sans-serif;color:var(--white)}
.frame{position:absolute;left:49px;top:49px;width:1102px;height:700px;border:3px solid var(--lime);border-bottom:none}
.step-title{position:absolute;left:90px;top:74px;font-family:"Playfair Display",serif;font-weight:700;font-size:44px;color:var(--lime);letter-spacing:1px}
.step-label{position:absolute;left:52px;top:135px;width:355px;height:50px;background:var(--lime);color:var(--ink);font-size:21px;font-weight:500;letter-spacing:1.2px;line-height:50px;padding-left:38px}
.step-label b{font-weight:800}
.body-text{position:absolute;left:89px;font-size:21px;font-weight:500;letter-spacing:1.1px;line-height:29px;color:var(--white)}
.t1{top:201px}
.t2{top:261px;width:1040px}
.t3{top:657px}
.screen{position:absolute;left:87px;top:351px;width:1030px;height:289px;background:var(--ui-bg);font-family:"Inter",sans-serif;overflow:hidden}
.nav{position:absolute;top:13px;left:0;width:100%;height:18px}
.brand{position:absolute;left:17px;top:-2px;display:flex;align-items:center;gap:6px;color:var(--ui-yellow);font-weight:700;font-size:15px;letter-spacing:.5px}
.brand i{display:block;width:10px;height:10px;border-radius:50%;background:var(--ui-yellow)}
.nav-item{position:absolute;top:2px;font-size:10.5px;font-weight:600;color:var(--ui-text)}
.deposit{position:absolute;left:798px;top:9px;width:67px;height:25px;border-radius:4px;background:var(--ui-yellow);color:var(--ink);font-size:10.5px;font-weight:600;text-align:center;line-height:25px}
.icons{position:absolute;left:0;top:0}
.highlight{position:absolute;left:901px;top:2px;width:34px;height:39px;border:3px solid var(--marker)}
.hero{position:absolute;left:58px;top:102px;font-weight:700;font-size:46px;line-height:53px;color:var(--ui-text);letter-spacing:-.5px}
.hero span{color:var(--ui-yellow)}
.coins{position:absolute;left:610px;top:84px;width:375px;height:194px;border-radius:12px;background:var(--ui-panel)}
.coin{position:absolute;left:18px;width:338px;height:22px;font-size:11px;font-weight:600;color:var(--ui-text)}
.coin .dot{position:absolute;left:0;top:0;width:21px;height:21px;border-radius:50%}
.coin .name{position:absolute;left:28px;top:4px}
.coin .name em{font-style:normal;font-weight:500;color:var(--ui-muted)}
.coin .price{position:absolute;right:93px;top:4px}
.coin .change{position:absolute;right:0;top:4px;color:var(--ui-red)}
.view-all{position:absolute;left:18px;top:169px;font-size:9.5px;color:var(--ui-muted);font-weight:500}
.footer-band{position:absolute;left:0;top:727px;width:1200px;height:43px;background:var(--lime);color:var(--ink);font-size:21px;font-weight:800;letter-spacing:1.3px;line-height:43px;padding-left:90px}
</style>
</head>
<body>
<div class="page">
  <div class="frame"></div>
  <h1 class="step-title">STEP 3</h1>
  <div class="step-label">OPEN <b>FUTURES ACCOUNT</b></div>

  <p class="body-text t1">If you have already opened a Futures account, you can skip this step.</p>
  <p class="body-text t2">Once you are connected, move your mouse over the second icon on the top right area of the screen.</p>

  <div class="screen">
    <div class="nav">
      <div class="brand"><i></i>VANTREX</div>
      <span class="nav-item" style="left:128px">Buy Crypto</span>
      <span class="nav-item" style="left:201px">Markets</span>
      <span class="nav-item" style="left:260px">Trade ⌄</span>
      <span class="nav-item" style="left:318px">Futures ⌄</span>
      <span class="nav-item" style="left:387px">Earn</span>
      <span class="nav-item" style="left:429px">Square ⌄</span>
      <span class="nav-item" style="left:495px">More ⌄</span>
    </div>
    <div class="deposit">⤓ Deposit</div>
    <svg class="icons" width="1030" height="100" viewBox="0 0 1030 100">
      <g fill="none" stroke="#eaecef" stroke-width="2">
        <circle cx="775" cy="20" r="5.5"/><line x1="779" y1="24" x2="783" y2="28"/>
      </g>
      <g fill="#eaecef">
        <circle cx="886" cy="21" r="7"/>
        <rect x="911" y="14" width="13" height="14" rx="2"/>
        <path d="M941 27h14l-2-3v-5a5 5 0 0 0-10 0v5z"/>
        <rect x="972" y="14" width="12" height="14" rx="1"/>
        <circle cx="1009" cy="21" r="7"/>
      </g>
      <circle cx="955" cy="14" r="2.5" fill="#f0b90b"/>
      <rect x="913" y="19" width="9" height="2" fill="#171a1f"/>
      <g stroke="#171a1f" stroke-width="1.5"><line x1="1009" y1="14" x2="1009" y2="28"/><line x1="1002" y1="21" x2="1016" y2="21"/></g>
      <line x1="831" y1="75" x2="888" y2="47" stroke="#ff2a1a" stroke-width="3"/>
      <path d="M898 42l-17 1 7 12z" fill="#ff2a1a"/>
    </svg>
    <div class="highlight"></div>

    <h2 class="hero"><span>Get Verified</span> and<br>Start Your Crypto<br>Journey</h2>

    <div class="coins">
      <div class="coin" style="top:20px"><i class="dot" style="background:#f7931a"></i><span class="name">ORV <em>Orvane</em></span><span class="price">$51,000.28</span><span class="change">-1.37%</span></div>
      <div class="coin" style="top:57px"><i class="dot" style="background:#6f7fe6"></i><span class="name">PLX <em>Pellix</em></span><span class="price">$2,932.03</span><span class="change">-2.13%</span></div>
      <div class="coin" style="top:94px"><i class="dot" style="background:#f0b90b"></i><span class="name">VTX <em>VTX</em></span><span class="price">$377.80</span><span class="change">-0.50%</span></div>
      <div class="coin" style="top:131px"><i class="dot" style="background:#2b3139"></i><span class="name">KLR <em>Kelora</em></span><span class="price">$0.5364</span><span class="change">-1.56%</span></div>
      <div class="view-all">View All 350+ Coins ›</div>
    </div>
  </div>

  <p class="body-text t3">Select “Futures” on the drop-down list that appears.</p>

  <div class="footer-band">BRINDLEQUAY COPY TRADING TUTORIAL</div>
</div>
</body>
</html>
```